Maren Holt Luxury Wellness Profile Booklet

I am a luxury wellness property agent and would like to create my personal profile booklet. I want this to feel luxurious, minimalist, informative and the philosophy behind wellness and property the cPAGE 1 — THE COVER

Very minimal.

MAREN HOLT

LUXURY WELLNESS PROPERTY

PROPERTY • WELLNESS • LIFESTYLE

Fenwick Dale Coastline Group

Large photograph of you — preferably walking through a beautiful waterfront property or standing naturally within an architectural setting.

At the bottom:

Hope Island • Sanctuary Cove • Helensvale

Small Fenwick Dale logo.

PAGE 2 — THE OPENING STATEMENT

A beautiful full-page lifestyle photograph.

Overlaid:

WHERE PROPERTY
MEETS WELLBEING

“A home is more than an address. It is the environment in which life unfolds.”

Then a short introduction:

Opening Profile

I believe the most exceptional properties are not defined simply by their architecture, address or price.

They are defined by how they make you feel.

Natural light. Water views. Privacy. Green space. Indoor-outdoor living. A place to unwind, entertain, recharge and reconnect.

My approach to luxury property brings these elements together — combining strategic real estate expertise with a genuine understanding of wellness, lifestyle and the way people want to live today.

Because when we understand the lifestyle behind the property, we can create a more compelling story around it.

PAGE 3 — MEET MAREN

Large portrait of you on one side.

Other side:

MEET MAREN

20+ YEARS OF PROPERTY EXPERIENCE

Commercial
Residential
Project Sales
Luxury & Lifestyle Property

Then:

About Maren

With more than 20 years' experience across commercial, residential and project sales, I have built my career around relationships, strategic marketing and delivering exceptional outcomes for my clients.

My approach is warm, considered and highly personal.

I believe sellers deserve more than a listing campaign. They deserve a clear strategy, honest communication and an agent who understands what makes their property valuable — both financially and emotionally.

Today, my focus is luxury lifestyle property across the Northern Gold Coast, with a particular passion for Hope Island, Sanctuary Cove and selected waterfront gated estates in Helensvale.

PAGE 4 — WHY WELLNESS?

This is where your differentiation becomes really powerful.

Full-bleed photograph of:

pool
outdoor entertaining
greenery
water
spa
wellness room
person walking beside water
WELLNESS IS THE NEW LUXURY

Then:

Wellness Philosophy

Luxury has evolved.

Today, luxury is not only about beautiful finishes, expansive living spaces or an impressive address.

It is privacy.

It is waking to water.

It is natural light flooding through the home.

It is having space to breathe.

It is stepping outside into nature, walking along the water, enjoying a morning swim, entertaining beside the pool or creating a private sanctuary at home.

These lifestyle elements increasingly shape the way buyers experience and value a property.

This is where my passion for wellness becomes part of my property approach.

PAGE 5 — MY WELLNESS JOURNEY

This page makes the wellness positioning credible rather than simply being a marketing slogan.

MY WELLNESS JOURNEY

You could use 3 small photographs:

BLOOMTOT CO
SOLACE WELLNESS CENTRE
LUXURY WELLNESS PROPERTY

Copy:

Wellness Journey

My connection with wellness began outside of real estate.

After stepping away from property, I founded Bloomtot Co, developing an organic children's nutritional product with a focus on natural ingredients and wellbeing.

I later launched Solace Wellness Centre, further deepening my understanding of wellness, health-conscious lifestyles and the importance of creating environments that support how we live.

Today, I bring that perspective back into property.

I see homes differently — not simply as buildings, but as environments for living, restoring, entertaining and thriving.

PAGE 6 — THE MAREN HOLT DIFFERENCE

This should be one of your strongest pages.

A DIFFERENT WAY OF SEEING PROPERTY

Use six elegant icons or small images:

01 — LIFESTYLE

I look beyond the floor plan to understand how buyers will actually experience the home.

02 — WELLNESS

I identify the spaces and features that contribute to wellbeing and lifestyle.

03 — PRESENTATION

I create a campaign that makes the property feel aspirational, memorable and emotionally engaging.

04 — STORY

Every exceptional property has a story. I find it, refine it and communicate it.

05 — STRATEGY

From positioning and buyer targeting to campaign execution and negotiation, every element has a purpose.

06 — RELATIONSHIPS

Trust, transparency and communication remain at the centre of every campaign.

PAGE 7 — YOUR PROPERTY STORY

This could be a beautiful editorial spread.

EVERY HOME HAS A STORY

Then:

My role is to discover what makes yours extraordinary.

Three questions:

WHAT MAKES YOUR PROPERTY DIFFERENT?

Architecture?
Waterfront?
Views?
Privacy?
Garden?
Location?

HOW DOES IT MAKE PEOPLE FEEL?

Calm?
Inspired?
Connected?
Entertained?
Relaxed?

WHO WILL FALL IN LOVE WITH IT?

Families?
Executives?
Downsizers?
Boaties?
Golfers?
Wellness-focused buyers?
Lifestyle purchasers?

Then:

I turn these answers into your property's story.

PAGE 8 — YOUR NORTHERN GOLD COAST

Beautiful aerial/waterfront image.

MY MARKET

HOPE ISLAND

SANCTUARY COVE

HELENSVALE

WATERFRONT & GATED ESTATES

Copy:

Northern Gold Coast

I specialise in the lifestyle-driven property market of the Northern Gold Coast.

From the waterfront homes and private enclaves of Hope Island and Sanctuary Cove to the established gated estates of Helensvale, I understand the lifestyle characteristics that attract buyers to this part of the Gold Coast.

Having personally experienced the lifestyle of these communities, I understand that buyers are often purchasing far more than a house.

They are buying a way of life.

PAGE 9 — THE WELLNESS PROPERTY

This could become your signature page.

WHAT MAKES A WELLNESS HOME?

Use a sophisticated grid:

WATER
Pools • Waterfront • Marina • Water views

NATURE
Green space • Gardens • Reserve outlooks • Walking trails

LIGHT
Natural light • Orientation • Open spaces

MOVEMENT
Walking • Golf • Boating • Outdoor living

RESTORATION
Spa • Sauna • Cold plunge • Retreat spaces

CONNECTION
Entertaining • Family • Indoor/outdoor living

Bottom:

The most desirable luxury is often the way a home makes you feel.

PAGE 10 — THE SELLING EXPERIENCE
YOUR HOME. YOUR STORY. YOUR CAMPAIGN.

I would make this a simple six-stage journey:

01 — DISCOVER
Understand your property, your goals and your lifestyle.

↓

02 — POSITION
Establish the property's unique market position.

↓

03 — PREPARE
Presentation, styling and strategic recommendations.

↓

04 — CREATE
Photography, film, editorial storytelling and digital marketing.

↓

05 — CONNECT
Targeted buyer engagement and database activation.

↓

06 — NEGOTIATE
Strategic negotiation designed to maximise the opportunity.

PAGE 11 — THE POWER OF PRESENTATION

Large before/after style photography.

FIRST IMPRESSIONS ARE EVERYTHING

Copy:

We don't get a second opportunity to create a first impression.

Then explain your approach to:

styling
photography
cinematic video
twilight imagery
aerial photography
lifestyle storytelling
digital advertising
targeted database marketing
buyer follow-up
auction strategy

Importantly, don't make this page feel like a generic list of marketing products.

Frame everything around:

Creating desire before creating urgency.
PAGE 12 — PROVEN RESULTS

Now introduce your actual results.

RESULTS THAT BUILD CONFIDENCE

Use your strongest results as elegant case studies.

For example:
4183 Palmetto Drive, Hope Island
$3,850,000
34 Days On The Market

$2.90M
71 Heron Bay Boulevard, Helensvale
Sold within 45 days

Include your result and the property's story.

$2.15M

3/9 Heron Bay Boulevard

Waterfront Villa

Then potentially:

28 DAYS

5419 Quaywood Boulevard, Hope Island

Under contract following relaunch

If a result subsequently changed because the contract fell through, be careful about how you describe the current status. We can make this page completely accurate to the final outcome.

PAGE 13 — THE FENWICK DALE ADVANTAGE

This is where you let the brand support you, rather than letting the booklet become a Fenwick Dale corporate brochure.

PERSONAL SERVICE.
NATIONAL REACH.

Then a short statement about your Fenwick Dale platform.

You could include:

POWERFUL BUYER DATABASE

LUXURY PROPERTY MARKETING

AUCTION EXPERTISE

DIGITAL REACH

LOCAL KNOWLEDGE

NATIONAL NETWORK

And a short line:

The personal attention of a specialist agent, supported by the strength of a globally recognised property network.

PAGE 14 — WHAT YOU CAN EXPECT FROM ME

This page is very important for your seller proposition.

MY PROMISE TO YOU

TRANSPARENCY

Clear advice, honest feedback and no unnecessary promises.

COMMUNICATION

You will know what is happening throughout your campaign.

STRATEGY

Every decision is made with your property, market and objectives in mind.

ATTENTION TO DETAIL

Your home deserves meticulous preparation and presentation.

PERSONAL SERVICE

You deal directly with me throughout your campaign.

RESULT FOCUS

My role is to create the strongest possible environment for a successful sale.

PAGE 15 — THE CLOSING PAGE

This should be very luxurious and emotional.

Beautiful photograph of water at sunset / luxury pool / Hope Island lifestyle.

YOUR HOME.
YOUR NEXT CHAPTER.

Then:

Closing Statement

Selling a home is rarely just a transaction.

It is the closing of one chapter and the beginning of another.

My role is to make the journey feel considered, strategic and personal — while creating the strongest possible opportunity for your property in the marketplace.

Thank you for considering me to represent your home.

I would be honoured to tell its story.

Then your details:

MAREN HOLT

Luxury Wellness Property

0412 557 830

BACK COVER

Keep it extremely clean.

Your photograph or perhaps a beautiful Gold Coast waterfront image.

MAREN HOLT

LUXURY WELLNESS PROPERTY

0412 557 830

Fenwick Dale logoollaboration. I can send a full brief if required.

Target Market(s)

Luxury Property Owners

Industry/Entity Type

Wellness Luxury Real Estate Lifestyle

Requirements
Must have
• A luxurious minimalist clean feel

```html
<!DOCTYPE html>
<html lang="en">
<head>
<meta charset="utf-8">
<title>Maren Holt — Luxury Wellness Profile</title>
<link rel="stylesheet" href="https://fonts.googleapis.com/css2?family=Libre+Caslon+Text:ital,wght@0,400;0,700;1,400&family=Montserrat:wght@400;500;600;700&display=swap">
<style>
  :root {
    --stage: #231f18;
    --paper: #f4f2ee;
    --white: #ffffff;
    --navy: #1d2a34;
    --ink: #16191d;
    --ink-soft: #2c3136;
    --slate: #6f8191;
    --mist: #a9b7c2;
    --yellow: #f3e01c;
    --rule: #3c4a55;
    --serif: "Libre Caslon Text", Georgia, serif;
    --sans: "Montserrat", Arial, sans-serif;
  }
  * { box-sizing: border-box; margin: 0; padding: 0; }
  html, body { width: 1196px; height: 1200px; overflow: hidden; }
  body {
    background: var(--stage);
    font-family: var(--sans);
    display: flex;
    align-items: center;
    justify-content: center;
  }
  .spread { display: flex; gap: 22px; }
  .page {
    position: relative;
    width: 372px;
    height: 526px;
    overflow: hidden;
  }
  .eyebrow {
    position: absolute;
    font-family: var(--sans);
    font-size: 5.5px;
    font-weight: 700;
    letter-spacing: 0.14em;
    text-transform: uppercase;
  }
  .eyebrow--dash::before {
    content: "";
    display: inline-block;
    width: 12px;
    height: 3px;
    background: var(--yellow);
    margin-right: 7px;
    vertical-align: middle;
  }
  .folio {
    position: absolute;
    right: 22px;
    bottom: 18px;
    font-size: 5px;
    font-weight: 700;
    display: flex;
    align-items: center;
    gap: 5px;
  }
  .folio::before { content: ""; width: 22px; height: 1px; background: currentColor; opacity: .6; }

  /* Cover */
  .cover { background: var(--paper); color: var(--ink); }
  .cover__band { position: absolute; top: 0; left: 0; right: 0; height: 7px; background: var(--yellow); }
  .cover .eyebrow { top: 22px; left: 24px; color: var(--ink); }
  .cover__name {
    position: absolute; top: 40px; left: 22px;
    font-family: var(--serif); font-weight: 700; font-size: 31px; letter-spacing: .01em;
  }
  .cover__role {
    position: absolute; top: 86px; left: 24px;
    font-family: var(--serif); font-size: 8.5px; letter-spacing: .08em; color: var(--slate);
  }
  .cover__photo {
    position: absolute; top: 108px; left: 27px; width: 318px; height: 314px;
    border: 1.5px solid var(--ink);
    background: linear-gradient(120deg, #e6ddd2 0%, #efe8df 45%, #d9cfc3 100%);
  }
  .cover__footer {
    position: absolute; top: 440px; left: 27px; width: 318px; height: 66px;
    background: var(--ink); color: var(--white); padding: 11px 12px;
  }
  .cover__pillars { font-size: 5.5px; font-weight: 600; letter-spacing: .16em; }
  .cover__places { font-size: 6px; margin-top: 18px; }
  .cover__group { font-size: 5.5px; margin-top: 5px; opacity: .85; }
  .brand {
    position: absolute; right: 12px; bottom: 14px;
    display: flex; align-items: center; gap: 5px;
    font-family: var(--sans); font-size: 7px; font-weight: 700; color: var(--white);
  }
  .brand__mark { width: 8px; height: 8px; background: var(--yellow); }

  /* Opening statement */
  .opening { background: var(--navy); color: var(--white); }
  .opening .eyebrow { top: 32px; left: 27px; color: #c9d1d7; }
  .opening__photo {
    position: absolute; top: 0; left: 197px; width: 175px; height: 268px;
    background: linear-gradient(180deg, #f2a84a 0%, #c98a5a 28%, #5f6b4a 46%, #3f6f8e 62%, #6fb3dc 82%, #8ec6e6 100%);
  }
  .opening__edge { position: absolute; top: 0; left: 193px; width: 4px; height: 268px; background: var(--yellow); }
  .opening__title {
    position: absolute; top: 62px; left: 26px;
    font-family: var(--serif); font-size: 19px; line-height: 1.08; letter-spacing: .04em; font-weight: 400;
  }
  .opening__quote {
    position: absolute; top: 143px; left: 27px; width: 158px;
    font-family: var(--serif); font-size: 7.5px; line-height: 1.4; color: #c8d0d6;
  }
  .opening__rule { position: absolute; top: 290px; left: 27px; right: 22px; height: 1px; background: var(--rule); }
  .opening__label {
    position: absolute; top: 310px; left: 27px;
    font-size: 6.5px; font-weight: 600; letter-spacing: .14em; color: var(--yellow);
  }
  .opening__cols {
    position: absolute; top: 336px; left: 27px; right: 22px;
    display: grid; grid-template-columns: 1fr 1fr; gap: 20px;
    font-size: 4.6px; line-height: 1.45; color: #dfe4e8;
  }
  .opening__cols p + p { margin-top: 5px; }
  .opening .folio { color: #c9d1d7; }

  /* Meet Maren */
  .meet { background: var(--white); color: var(--ink); }
  .meet__photo {
    position: absolute; top: 0; left: 0; width: 158px; height: 526px;
    background: linear-gradient(160deg, #e9e3da 0%, #d8cdc0 55%, #c9bcad 100%);
  }
  .meet__edge { position: absolute; top: 0; left: 158px; width: 4px; height: 526px; background: var(--yellow); }
  .meet .eyebrow { top: 32px; left: 186px; color: var(--slate); }
  .meet__stat {
    position: absolute; top: 52px; left: 184px;
    font-family: var(--serif); font-size: 44px; color: var(--mist); line-height: 1;
  }
  .meet__stat-label {
    position: absolute; top: 104px; left: 186px;
    font-size: 4.5px; font-weight: 600; letter-spacing: .14em; color: var(--slate);
  }
  .meet__list { position: absolute; top: 134px; left: 186px; list-style: none; }
  .meet__list li {
    display: flex; align-items: center; gap: 8px;
    font-size: 5px; font-weight: 700; letter-spacing: .08em; text-transform: uppercase;
    margin-bottom: 12px;
  }
  .meet__list li::before { content: ""; width: 6px; height: 6px; background: var(--yellow); }
  .meet__rule { position: absolute; top: 226px; left: 186px; right: 22px; height: 1px; background: #d7dadd; }
  .meet__about-title {
    position: absolute; top: 240px; left: 186px;
    font-size: 5px; font-weight: 700; letter-spacing: .08em;
  }
  .meet__about {
    position: absolute; top: 258px; left: 186px; right: 22px;
    font-size: 4.4px; line-height: 1.5; font-weight: 500; color: var(--ink-soft);
  }
  .meet__about p + p { margin-top: 6px; }
  .meet .folio { color: var(--ink); }
</style>
</head>
<body>
<main class="spread">

  <section class="page cover">
    <div class="cover__band"></div>
    <p class="eyebrow">Personal Profile • Northern Gold Coast</p>
    <h1 class="cover__name">MAREN HOLT</h1>
    <p class="cover__role">LUXURY WELLNESS PROPERTY</p>
    <div class="cover__photo" role="img" aria-label="Portrait of Maren Holt walking down a light stone staircase in an architectural home"></div>
    <div class="cover__footer">
      <p class="cover__pillars">PROPERTY &nbsp;/&nbsp; WELLNESS &nbsp;/&nbsp; LIFESTYLE</p>
      <p class="cover__places">Hope Island / Sanctuary Cove / Helensvale</p>
      <p class="cover__group">Fenwick Dale Coastline Group</p>
      <div class="brand"><span class="brand__mark"></span>Fenwick Dale</div>
    </div>
  </section>

  <section class="page opening">
    <p class="eyebrow eyebrow--dash">The Opening Statement</p>
    <h2 class="opening__title">WHERE<br>PROPERTY<br>MEETS<br>WELLBEING</h2>
    <p class="opening__quote">“A home is more than an address. It is the environment in which life unfolds.”</p>
    <div class="opening__edge"></div>
    <div class="opening__photo" role="img" aria-label="Waterfront pool at sunset with trees reflected in the canal"></div>
    <div class="opening__rule"></div>
    <p class="opening__label">OPENING PROFILE</p>
    <div class="opening__cols">
      <div>
        <p>I believe the most exceptional properties are not defined simply by their architecture, address or price.</p>
        <p>They are defined by how they make you feel.</p>
        <p>Natural light. Water views. Privacy. Green space. Indoor-outdoor living. A place to unwind, entertain, recharge and reconnect.</p>
      </div>
      <div>
        <p>My approach to luxury property brings these elements together — combining strategic real estate expertise with a genuine understanding of wellness, lifestyle and the way people want to live today.</p>
        <p>Because when we understand the lifestyle behind the property, we can create a more compelling story around it.</p>
      </div>
    </div>
    <p class="folio">02</p>
  </section>

  <section class="page meet">
    <div class="meet__photo" role="img" aria-label="Portrait of Maren Holt seated on a sculptural stone stool"></div>
    <div class="meet__edge"></div>
    <p class="eyebrow eyebrow--dash">Meet Maren</p>
    <p class="meet__stat">20+</p>
    <p class="meet__stat-label">YEARS OF PROPERTY EXPERIENCE</p>
    <ul class="meet__list">
      <li>Commercial</li>
      <li>Residential</li>
      <li>Project Sales</li>
      <li>Luxury &amp; Lifestyle Property</li>
    </ul>
    <div class="meet__rule"></div>
    <p class="meet__about-title">ABOUT MAREN</p>
    <div class="meet__about">
      <p>With more than 20 years' experience across commercial, residential and project sales, I have built my career around relationships, strategic marketing and delivering exceptional outcomes for my clients.</p>
      <p>My approach is warm, considered and highly personal.</p>
      <p>I believe sellers deserve more than a listing campaign. They deserve a clear strategy, honest communication and an agent who understands what makes their property valuable — both financially and emotionally.</p>
      <p>Today, my focus is luxury lifestyle property across the Northern Gold Coast, with a particular passion for Hope Island, Sanctuary Cove and selected waterfront gated estates in Helensvale.</p>
    </div>
    <p class="folio">03</p>
  </section>

</main>
</body>
</html>
```